High End Skincare for Women Cosmetics Brand

We need a wordpress website that is also a mobile-friendly website for our cosmetics company. We have 3 core products and have 10 dropship products to add. I have attached the pdf with brand guide and vision for the website.

Our mission - At Mira Vale we believe all women have four distinct characteristics; beauty, originality, passion, and confidence. Our beauty products simply enhance those qualities. We will always provide the safest products to our consumers and continue to uplift women around the world.

About us - MIRA VALE IS AN ORGANIC COSMETICS AND SKINCARE BRAND WITH VARIOUS PRODUCTS TO ENHANCE YOUR NATURAL BEAUTY. WE ARE COMMITTED TO PROVIDING TIMELESS PRODUCTS THAT WILL BRING OUT THAT SPECIAL CONFIDENCE YOU FEEL AND DESIRE FROM COSMETICS THAT WILL PERFECTLY MESH YOUR LIFESTYLE. When you choose Mira Vale organic cosmetics and skincare products, you are choosing a product whose ingredients work perfectly with the most complicated natural skin. We want you to celebrate that unique natural beauty with Mira Vale organic cosmetics and skincare products that will enhance your beauty. We use the best quality plant-based and laboratory-made ingredients to produce the best organic products that will enhance your beauty and boost your confidence.

XoXo Mira Vale - We understand that beauty is much more than an outward appearance. Our unique products bring you confidence, courage, and enrich your spirit. True beauty is deeper, and we at Mira Vale seek to inspire you to discover that deep sense of beauty you always craved.

Style - Luxury High End / Should look expensive and feminine with a modern touch.
The logo files are attached to this.

Colors should be bold and bright that looks like luxury and modern.

The products we sell are organic skincare and cosmetic products.

The design should not include any images or generic types of a font that can be found in Microsoft Word.

Premium font required.

Mira Vale is a leading organic cosmetics and skincare brand with products that enhance the natural beauty of the everyday woman. Luxury without the luxe price tag.

Target Market(s)

Target audience women age 18- 42 Gen Y / Millennials / Gen X

Industry/Entity Type

Beauty

Number of Pages Required

4 page

Font styles to use
Sans Serif

Colors

Designer to choose colors to be used in the design.

Requirements
Must have
• Must have images of women of diverse ethnicity at least 4 women
• Must have images of products -
• Must have an option to integrate dropship product links
• Must have contact us form
• Must have about us page
• Must have high-resolution images
• Must have a feature to check out on the website
• Must be mobile friendly
Nice to have
• Nice to have blog feature
• Nice to have a chat bot

```html
<!DOCTYPE html>
<html lang="en">
<head>
<meta charset="utf-8">
<title>Mira Vale — Organic Skincare</title>
<link rel="stylesheet" href="https://fonts.googleapis.com/css2?family=Montserrat:wght@400;500;600&family=Lato:wght@400;700&display=swap">
<style>
:root{
  --ink:#141414;
  --night:#0d0c18;
  --rose:#ee4f6d;
  --grey:#7b7b7b;
  --line:#d9d9d9;
  --mist:#f3f3f3;
  --card-rose:#f2e4e7;
  --card-lilac:#e6e6f3;
  --card-mint:#e1eff0;
  --white:#ffffff;
}
*{box-sizing:border-box;margin:0;padding:0}
html,body{width:1200px;height:3394px;overflow:hidden}
body{position:relative;background:var(--white);color:var(--ink);font-family:"Lato",sans-serif}
.abs{position:absolute}
.head-font{font-family:"Montserrat",sans-serif}

/* hero */
.hero{left:0;top:0;width:1200px;height:566px;background:var(--night)}
.hero-photo{right:0;top:0;width:680px;height:566px;background:linear-gradient(100deg,var(--night) 0%,#3a2a2a 30%,#a27d68 55%,#c89b80 75%,#6d4a3a 100%)}
.brand{font-family:"Montserrat",sans-serif;font-weight:400;letter-spacing:8px;text-transform:uppercase}
.nav-brand{left:97px;top:18px;color:var(--white);font-size:26px}
.nav{top:22px;left:362px;display:flex;gap:0;color:var(--white);font-family:"Montserrat",sans-serif;font-weight:500;font-size:15px}
.nav a{position:absolute;white-space:nowrap;color:inherit;text-decoration:none}
.nav-tools{top:20px;left:916px;color:var(--white);font-family:"Montserrat",sans-serif;font-size:10px;display:flex;align-items:center}
.hero-title{left:120px;top:146px;color:var(--white);font-family:"Montserrat",sans-serif;font-weight:600;font-size:47px;line-height:54px}
.mark{position:relative;display:inline-block}
.mark::after{content:"";position:absolute;left:0;right:-4px;bottom:5px;height:5px;background:var(--rose)}
.mark span{position:relative;z-index:1}
.btn-solid{left:122px;top:358px;width:245px;height:56px;background:var(--rose);color:var(--white);font-family:"Montserrat",sans-serif;font-weight:600;font-size:15px;display:flex;align-items:center;justify-content:center;letter-spacing:.5px}

/* headings */
.section-title{left:0;width:1200px;text-align:center;font-family:"Montserrat",sans-serif;font-weight:500;font-size:46px}

/* products */
.card-bg{}
.product-shot{background:linear-gradient(180deg,#2a2a2a,#0c0c0c);border-radius:8px}
.product-name{font-family:"Montserrat",sans-serif;font-size:20px;color:#333}
.price{font-family:"Montserrat",sans-serif;font-weight:600;font-size:21px}
.stars{display:flex;gap:2px}
.btn-outline{width:244px;height:56px;border:2px solid var(--ink);font-family:"Montserrat",sans-serif;font-weight:600;font-size:15px;display:flex;align-items:center;justify-content:center}

/* welcome */
.group-photo{left:136px;top:1472px;width:579px;height:418px;background:linear-gradient(90deg,#e9d6c4 0%,#c79a7e 40%,#8a5a44 55%,#e3c7b4 80%,#f1e2d6 100%)}
.welcome-title{left:851px;top:1540px;font-family:"Montserrat",sans-serif;font-weight:500;font-size:44px;line-height:54px}
.welcome-copy{left:851px;top:1675px;width:240px;font-size:15px;line-height:24px;color:var(--grey)}
.learn-more{left:851px;top:1783px;font-size:13px;color:var(--rose);display:flex;align-items:center;gap:8px}

.perks{left:0;top:1890px;width:1200px;height:102px;background:var(--mist)}
.perk{top:1920px;display:flex;gap:18px;align-items:flex-start}
.perk h4{font-family:"Lato",sans-serif;font-weight:400;font-size:17px;color:#333}
.perk p{font-size:13px;color:var(--rose);margin-top:3px}

/* blog */
.post-photo{width:283px;height:211px}
.post-date{font-size:15px;color:var(--grey)}
.post-title{font-family:"Lato",sans-serif;font-weight:400;font-size:23px;line-height:30px;width:290px}
.post-excerpt{font-size:15px;line-height:24px;color:#444;width:280px}

/* contact */
.contact-title{left:199px;top:2775px;font-family:"Montserrat",sans-serif;font-weight:600;font-size:47px;line-height:55px}
.contact-line{left:199px;font-size:13px;color:var(--grey);display:flex;align-items:center;gap:14px}
.field{border:1px solid var(--line);background:#f7f7f7;font-size:11px;color:#9a9a9a;display:flex;align-items:center;gap:10px;padding-left:14px}
.field.area{align-items:flex-start;padding-top:14px}
.btn-send{left:582px;top:3016px;width:140px;height:40px;background:var(--rose);color:var(--white);font-family:"Montserrat",sans-serif;font-weight:600;font-size:10px;letter-spacing:2px;display:flex;align-items:center;justify-content:center}

/* footer */
.footer-brand{left:0;width:1200px;top:3178px;text-align:center;font-size:28px;color:var(--ink)}
.follow{left:490px;top:3256px;display:flex;align-items:center;gap:22px;font-size:12px;font-family:"Montserrat",sans-serif}
.social{width:14px;height:14px;border-radius:50%;background:var(--ink)}
.legal{left:0;top:3323px;width:1200px;height:71px;background:#f0f0f0;font-size:12px;color:#333}
.legal span{position:absolute;top:29px}
.pay{width:24px;height:14px;border-radius:2px;background:#555;display:inline-block}
</style>
</head>
<body>

<!-- Hero -->
<section class="abs hero" aria-label="Hero">
  <div class="abs hero-photo" role="img" aria-label="Portrait photograph of a woman with long wavy hair"></div>
  <div class="abs nav-brand brand">Mira Vale</div>
  <nav class="abs nav" style="left:0;width:1200px;height:30px">
    <a style="left:362px">HOME</a>
    <a style="left:444px">PRODUCTS</a>
    <a style="left:564px">TUTORIALS</a>
    <a style="left:686px">BLOG</a>
    <a style="left:763px">CONTACT</a>
  </nav>
  <div class="abs nav-tools">
    <svg width="16" height="16" viewBox="0 0 16 16" fill="none" stroke="#fff" stroke-width="1.6"><circle cx="6.5" cy="6.5" r="5"/><path d="M10.5 10.5L15 15"/></svg>
    <span style="margin-left:14px;border-left:1px solid #777;height:22px"></span>
    <span style="margin-left:12px">ENG ▾</span>
    <span style="margin-left:16px">USD ▾</span>
    <svg style="margin-left:44px" width="18" height="18" viewBox="0 0 18 18" fill="none" stroke="#fff" stroke-width="1.5"><path d="M3 6h12l-1 10H4z"/><path d="M6.5 6V4.5a2.5 2.5 0 0 1 5 0V6"/><circle cx="15" cy="13" r="3" fill="#ee4f6d" stroke="none"/></svg>
  </div>
  <h1 class="abs hero-title"><span class="mark"><span>enhance</span></span><br>the beauty<br>within</h1>
  <div class="abs btn-solid">SHOP NOW</div>
</section>

<!-- Products -->
<h2 class="abs section-title" style="top:656px">Our Products</h2>

<div class="abs" style="left:97px;top:820px;width:317px;height:323px;background:var(--card-rose)"></div>
<div class="abs product-shot" role="img" aria-label="Oil cleanser pump bottle" style="left:204px;top:765px;width:104px;height:270px;border-radius:10px 10px 16px 16px"></div>
<div class="abs product-name" style="left:104px;top:1168px">MIRA VALE Oil Cleanser</div>
<div class="abs price" style="left:106px;top:1203px">$19.99</div>

<div class="abs" style="left:462px;top:951px;width:317px;height:192px;background:var(--card-lilac)"></div>
<div class="abs product-shot" role="img" aria-label="Face moisturizer jar" style="left:546px;top:918px;width:148px;height:82px"></div>
<div class="abs product-name" style="left:470px;top:1168px">MIRA VALE Face Moisturizer</div>
<div class="abs price" style="left:470px;top:1203px">$15.99</div>

<div class="abs" style="left:806px;top:951px;width:317px;height:192px;background:var(--card-mint)"></div>
<div class="abs product-shot" role="img" aria-label="Charcoal mask jar" style="left:891px;top:918px;width:148px;height:82px"></div>
<div class="abs product-name" style="left:813px;top:1168px">MIRA VALE Charcoal Mask</div>
<div class="abs price" style="left:813px;top:1203px">$19.99</div>

<svg width="0" height="0" style="position:absolute"><defs><path id="star" d="M5 0l1.5 3.2 3.5.4-2.6 2.4.7 3.5L5 7.8 1.9 9.5l.7-3.5L0 3.6l3.5-.4z"/></defs></svg>
<div class="abs stars" style="left:335px;top:1209px"><svg width="64" height="10"><use href="#star" fill="#ee4f6d"/><use href="#star" x="13" fill="#ee4f6d"/><use href="#star" x="26" fill="#ee4f6d"/><use href="#star" x="39" fill="#ee4f6d"/><use href="#star" x="52" fill="#ccc"/></svg></div>
<div class="abs stars" style="left:700px;top:1209px"><svg width="64" height="10"><use href="#star" fill="#ee4f6d"/><use href="#star" x="13" fill="#ee4f6d"/><use href="#star" x="26" fill="#ee4f6d"/><use href="#star" x="39" fill="#ee4f6d"/><use href="#star" x="52" fill="#ccc"/></svg></div>
<div class="abs stars" style="left:1043px;top:1209px"><svg width="64" height="10"><use href="#star" fill="#ee4f6d"/><use href="#star" x="13" fill="#ee4f6d"/><use href="#star" x="26" fill="#ee4f6d"/><use href="#star" x="39" fill="#ee4f6d"/><use href="#star" x="52" fill="#ccc"/></svg></div>

<div class="abs btn-outline" style="left:478px;top:1309px">SHOP NOW</div>

<!-- Welcome -->
<div class="abs group-photo" role="img" aria-label="Photograph of three smiling women of diverse ethnicity"></div>
<h2 class="abs welcome-title"><span class="mark"><span>welcome</span></span><br>MIRA VALE</h2>
<p class="abs welcome-copy">We are your leading organic cosmetics and skincare brand that offer products that enhance and nourish your skin.</p>
<div class="abs learn-more">Learn more
  <svg width="12" height="12" viewBox="0 0 12 12"><circle cx="6" cy="6" r="6" fill="#ee4f6d"/><path d="M5 3.5L7.5 6 5 8.5" stroke="#fff" stroke-width="1.4" fill="none"/></svg>
</div>

<div class="abs perks"></div>
<div class="abs perk" style="left:113px">
  <svg width="34" height="26" viewBox="0 0 34 26" fill="none" stroke="#ee4f6d" stroke-width="1.6"><path d="M2 4h19v14H2zM21 9h6l5 5v4H21"/><circle cx="8" cy="20" r="3" fill="#fff"/><circle cx="26" cy="20" r="3" fill="#fff"/></svg>
  <div><h4>Free Shipping And Return</h4><p>All order over $50</p></div>
</div>
<div class="abs perk" style="left:480px">
  <svg width="32" height="30" viewBox="0 0 32 30" fill="none" stroke="#ee4f6d" stroke-width="1.6"><path d="M5 12a11 11 0 0 1 20-4"/><path d="M25 2v6h-6"/><path d="M27 18a11 11 0 0 1-20 4"/><path d="M7 28v-6h6"/></svg>
  <div><h4>100% Money Guarantee</h4><p>Secure payment</p></div>
</div>
<div class="abs perk" style="left:835px">
  <svg width="30" height="30" viewBox="0 0 30 30" fill="none" stroke="#ee4f6d" stroke-width="1.6"><circle cx="15" cy="16" r="11"/><path d="M15 10v6l4 3M4 6l5-4M26 6l-5-4"/></svg>
  <div><h4>Fast And Reliable Support</h4><p>Support 24/7</p></div>
</div>

<!-- Blog -->
<h2 class="abs section-title" style="top:2066px">Blog &amp; News</h2>

<div class="abs post-photo" role="img" aria-label="Portrait of a woman with curly hair on pink backdrop" style="left:120px;top:2178px;background:linear-gradient(135deg,#e7b3c9,#8a4f4a 55%,#f0c7d6)"></div>
<div class="abs post-date" style="left:147px;top:2405px">Mars 02, 2019</div>
<div class="abs post-title" style="left:147px;top:2432px">Lorem Ipsum</div>
<div class="abs post-excerpt" style="left:147px;top:2474px">Suspendisse nunc odio, varius et consectetur et, dignissim a dui. In luctus risus orci.</div>

<div class="abs post-photo" role="img" aria-label="Portrait of a blonde woman on grey backdrop" style="left:464px;top:2178px;background:linear-gradient(135deg,#9c9c9c,#e6d2b5 50%,#8f8f8f)"></div>
<div class="abs post-date" style="left:490px;top:2405px">Mars 01, 2019</div>
<div class="abs post-title" style="left:490px;top:2432px">Donec Lobortis</div>
<div class="abs post-excerpt" style="left:490px;top:2474px">Fusce eget enim at purus sagittis finibus ac ut nisl.</div>

<div class="abs post-photo" role="img" aria-label="Portrait of a woman with pink hair and manicure" style="left:797px;top:2178px;background:linear-gradient(135deg,#e6dcdc,#e0718f 45%,#f2e6e3)"></div>
<div class="abs post-date" style="left:823px;top:2405px">Mars 02, 2019</div>
<div class="abs post-title" style="left:823px;top:2432px">Ut Pellentesque Dui Vel Leo Facilisis</div>
<div class="abs post-excerpt" style="left:823px;top:2504px">Praesent scelerisque libero urna...</div>

<div class="abs btn-outline" style="left:478px;top:2594px">VIEW ALL</div>

<!-- Contact -->
<h2 class="abs contact-title"><span class="mark"><span>get in</span></span><br>touch<br>with us</h2>
<div class="abs contact-line" style="top:2972px">
  <svg width="12" height="12" viewBox="0 0 12 12"><path d="M2 1l2.5 0 1 3-1.5 1a7 7 0 0 0 3 3l1-1.5 3 1V11A10 10 0 0 1 1 2z" fill="#ee4f6d"/></svg>+1 555-014-2290</div>
<div class="abs contact-line" style="top:3005px">
  <svg width="12" height="10" viewBox="0 0 12 10"><rect width="12" height="10" rx="1" fill="#ee4f6d"/><path d="M0.5 1l5.5 4 5.5-4" stroke="#fff" fill="none"/></svg>hello@miravale.com</div>

<div class="abs field" style="left:582px;top:2789px;width:204px;height:41px">
  <svg width="11" height="12" viewBox="0 0 11 12"><circle cx="5.5" cy="3" r="3" fill="#999"/><path d="M0 12a5.5 5 0 0 1 11 0z" fill="#999"/></svg>Name</div>
<div class="abs field" style="left:797px;top:2789px;width:206px;height:41px">
  <svg width="13" height="10" viewBox="0 0 13 10"><rect width="13" height="10" rx="1" fill="#999"/><path d="M0.5 1l6 4 6-4" stroke="#f7f7f7" fill="none"/></svg>E-mail</div>
<div class="abs field area" style="left:582px;top:2843px;width:421px;height:157px">Your Message</div>
<div class="abs btn-send">SEND</div>

<!-- Footer -->
<div class="abs footer-brand brand">Mira Vale</div>
<div class="abs follow">FOLLOW
  <span class="social"></span><span class="social"></span><span class="social"></span><span class="social"></span><span class="social"></span>
</div>

<footer class="abs legal">
  <span style="left:97px">© 2019 MIRA VALE. All rights reserved.</span>
  <span style="left:460px">Payment Options:</span>
  <span style="left:588px;top:28px;display:flex;gap:12px"><i class="pay"></i><i class="pay"></i><i class="pay"></i><i class="pay"></i></span>
  <span style="left:922px">Terms of Use</span>
  <span style="left:1024px">Privacy Policy</span>
</footer>

</body>
</html>
```